Real eatate

My company name is “Silver Heron Realestate” i would like to create a business card. I would like something modern and sleek similar to picture uploaded. All text in the business card should be black and the logo gold any shade.

```html
<!DOCTYPE html>
<html lang="en">
<head>
<meta charset="UTF-8">
<title>Silver Heron Realestate – Business Card</title>
<link rel="stylesheet" href="https://fonts.googleapis.com/css2?family=Source+Sans+3:wght@400;600;700&display=swap">
<style>
  :root {
    --backdrop: #e4e4e4;
    --card-dark: #151515;
    --card-light: #f4f4f4;
    --gold: #c9a232;
    --ink: #1c1c1c;
  }
  * { margin: 0; padding: 0; box-sizing: border-box; }
  html, body {
    width: 1200px; height: 960px; overflow: hidden;
    background: var(--backdrop);
    font-family: "Source Sans 3", Arial, sans-serif;
  }
  .canvas { position: relative; width: 1200px; height: 960px; }
  .card { position: absolute; left: 312px; width: 579px; height: 332px; }
  .card--front { top: 127px; background: var(--card-dark); }
  .card--back { top: 509px; background: var(--card-light); }

  .brand { position: absolute; text-align: center; }
  .brand__mark {
    display: block; margin: 0 auto;
    border-radius: 50%; background: var(--gold);
  }
  .brand__name {
    font-weight: 600; letter-spacing: 1.5px;
    line-height: 1.1; white-space: nowrap;
  }

  .card--front .brand { left: 0; right: 0; top: 82px; }
  .card--front .brand__mark { width: 100px; height: 100px; margin-bottom: 20px; }
  .card--front .brand__name { font-size: 26px; color: var(--gold); }

  .card--back .brand { left: 45px; top: 30px; }
  .card--back .brand__mark { width: 88px; height: 88px; margin-bottom: 14px; }
  .card--back .brand__name { font-size: 21px; color: var(--ink); }

  .agent { position: absolute; right: 38px; top: 143px; text-align: right; }
  .agent__name { color: var(--ink); font-weight: 700; font-size: 19px; line-height: 1.2; }
  .agent__title { color: var(--ink); font-size: 14px; line-height: 1.3; }

  .address {
    position: absolute; left: 45px; top: 192px;
    color: var(--ink); font-size: 15px; line-height: 19px; font-style: normal;
  }
  .contact { position: absolute; left: 45px; top: 237px; list-style: none; }
  .contact__item {
    display: flex; align-items: center; gap: 7px;
    color: var(--ink); font-size: 15px; line-height: 19.5px;
  }
  .contact__icon { width: 13px; height: 13px; fill: none; stroke: var(--gold); stroke-width: 1.4; }
  .contact__icon--filled { fill: var(--gold); stroke: none; }
</style>
</head>
<body>
<main class="canvas">
  <section class="card card--front" aria-label="Card front">
    <div class="brand">
      <span class="brand__mark" aria-hidden="true"></span>
      <p class="brand__name">Silver Heron Realestate</p>
    </div>
  </section>

  <section class="card card--back" aria-label="Card back">
    <div class="brand">
      <span class="brand__mark" aria-hidden="true"></span>
      <p class="brand__name">Silver Heron Realestate</p>
    </div>

    <div class="agent">
      <p class="agent__name">Daniel Carter</p>
      <p class="agent__title">REALTOR®</p>
    </div>

    <address class="address">
      450 N. E. 5th Street, Suite 310<br>
      Tampa, Florida, 33602
    </address>

    <ul class="contact">
      <li class="contact__item">
        <svg class="contact__icon contact__icon--filled" viewBox="0 0 24 24" aria-hidden="true"><path d="M6.6 10.8a15.1 15.1 0 0 0 6.6 6.6l2.2-2.2c.3-.3.7-.4 1-.2 1.1.4 2.3.6 3.6.6.6 0 1 .4 1 1V20c0 .6-.4 1-1 1A17 17 0 0 1 3 4c0-.6.4-1 1-1h3.5c.6 0 1 .4 1 1 0 1.3.2 2.5.6 3.6.1.3 0 .7-.2 1z"/></svg>
        (813) 555-0142
      </li>
      <li class="contact__item">
        <svg class="contact__icon" viewBox="0 0 24 24" aria-hidden="true"><rect x="2" y="5" width="20" height="14"/><path d="M2 5l10 8 10-8"/></svg>
        daniel@SilverHeron.com
      </li>
      <li class="contact__item">
        <svg class="contact__icon" viewBox="0 0 24 24" aria-hidden="true"><circle cx="12" cy="12" r="10"/><ellipse cx="12" cy="12" rx="4.5" ry="10"/><path d="M2 12h20M4 7h16M4 17h16"/></svg>
        www.SilverHeron.com
      </li>
    </ul>
  </section>
</main>
</body>
</html>
```